Bridal Beauty Expert 5 page Website

Modern 5 page website including: home page, Bridal Experts, services, gallery, and book me. Home page to include photo slideshow and contact information for stylist. The Bridal a Experts section will include short biography and photos of each bridal expert 3-4. Services page will include list and description of services and pricing. Gallery will contain work divided in the hair and makeup category. The book me page will contain an active booking tab with drop down service and customer information.

Target Market(s)

Brides, ages 21 to 45

Industry/Entity Type

Hair And Beauty

Coding

Coded - Design and coding required

Number of Pages Required

5+ page

Font styles to use
Serif
Decorative
Script

Colors
faa54b
97b8d9

Requirements
Must have
• Photo slideshow, photo gallery
Nice to have
• Scrolling slide show on home page

```html
<!DOCTYPE html>
<html lang="en">
<head>
<meta charset="utf-8">
<title>Lumen &amp; Lace — Bridal Hair and Makeup</title>
<link rel="stylesheet" href="https://fonts.googleapis.com/css2?family=Kaushan+Script&family=Lato:wght@400;700&family=Montserrat:wght@600;700&display=swap">
<style>
:root{
  --orange:#faa54b;
  --blue:#97b8d9;
  --ink:#0c0c0c;
  --panel:#1f1f1f;
  --text:#ffffff;
  --muted:#cfcfcf;
  --rule:#4a4a4a;
  --brown:#7a5530;
}
*{margin:0;padding:0;box-sizing:border-box}
html,body{width:1200px;height:2296px;overflow:hidden}
body{position:relative;background:var(--ink);color:var(--text);font-family:"Lato",sans-serif}
.abs{position:absolute}

/* hero */
.hero{left:0;top:0;width:1200px;height:729px;overflow:hidden;
  background:linear-gradient(90deg,#050505 0%,#0b0b0b 40%,#2a2f34 62%,#4a3b3a 80%,#1b2426 100%)}
.hero-photo{left:620px;top:0;width:580px;height:729px;
  background:radial-gradient(ellipse at 45% 35%,#c99682 0%,#8c5f52 30%,#2d2424 65%,rgba(10,10,10,0) 100%)}
.brush-photo{left:150px;top:180px;width:470px;height:549px;
  background:linear-gradient(180deg,rgba(150,110,80,.35),rgba(20,20,20,.9))}
.topband{left:0;top:64px;width:1200px;height:85px;background:rgba(151,184,217,.45)}
.mail{right:54px;top:18px;display:flex;align-items:center;gap:10px;font:700 15px "Lato",sans-serif}
.ring-icon{width:28px;height:28px;border:2px solid #fff;border-radius:50%;display:flex;align-items:center;justify-content:center}
.phone{left:752px;top:90px;display:flex;align-items:center;gap:14px;font:700 25px "Lato",sans-serif;letter-spacing:.5px}
.phone .ring-icon{width:32px;height:32px}
.book-btn{left:989px;top:86px;width:159px;height:41px;background:var(--orange);border:2px solid #fff;
  display:flex;align-items:center;justify-content:center;gap:12px;font:700 20px "Lato",sans-serif;color:#fff}
.brand{left:58px;top:88px;display:flex;align-items:center;gap:12px;font:700 30px "Lato",sans-serif;color:#fff;letter-spacing:.5px}
.brand i{width:18px;height:18px;border-radius:50%;background:var(--orange);display:block}
.nav-diamonds{left:0;top:0}
.nav-label{position:absolute;width:200px;text-align:center;font:700 19px "Montserrat",sans-serif;letter-spacing:.5px}
.nav-label svg{display:block;margin:0 auto 6px}
.nav-label.active::after{content:"";display:block;width:112px;height:2px;background:var(--orange);margin:6px auto 0}
.headline{left:250px;top:540px;width:700px;text-align:center;font:400 42px/56px "Kaushan Script",cursive}
.dots{left:560px;top:676px;display:flex;gap:12px;align-items:center}
.dots i{width:14px;height:14px;border-radius:50%;background:#fff;display:block}
.dots i.on{width:20px;height:20px;background:var(--orange)}

/* services */
.services{left:0;top:729px;width:1200px;height:438px;background:var(--ink)}
.service{position:absolute;top:70px;width:180px;text-align:center}
.service .badge{width:170px;height:170px;margin:0 auto;border-radius:50%;border:3px solid var(--orange);padding:8px}
.service .badge div{width:100%;height:100%;border-radius:50%;background:#fff;display:flex;align-items:center;justify-content:center}
.service h3{margin-top:30px;font:400 32px "Kaushan Script",cursive;color:var(--orange)}
.slider-rule{left:52px;width:1096px;height:1px;background:var(--rule)}
.arrow{width:34px;height:34px;border-radius:50%;background:#5a5a5a;display:flex;align-items:center;justify-content:center}

/* about */
.about{left:0;top:1167px;width:1200px;height:326px;background:var(--panel)}
.portrait{left:78px;top:47px;width:232px;height:232px;border-radius:50%;border:6px solid var(--blue);
  background:radial-gradient(circle at 50% 45%,#8a5a3c 0%,#4a2c1d 60%,#cfd6de 100%)}
.about h2{left:381px;top:53px;font:400 34px "Kaushan Script",cursive;color:var(--orange);letter-spacing:2px}
.about .title-rule{left:381px;top:104px;width:764px;height:1px;background:#555}
.about .copy{left:381px;top:128px;width:766px;font:400 14px/24px "Lato",sans-serif;color:#f2f2f2}
.about .copy p+p{margin-top:10px}

/* gallery */
.gallery h2{left:0;top:1540px;width:1200px;text-align:center;font:400 38px "Kaushan Script",cursive;color:var(--orange);letter-spacing:2px}
.shot{position:absolute}

/* footer */
.footer-nav{left:0;top:2079px;width:1200px;height:75px;background:var(--orange);color:#222}
.footer-nav ul{position:absolute;left:53px;top:28px;list-style:none;display:flex;font:400 15px "Lato",sans-serif}
.footer-nav li+li::before{content:"|";margin:0 16px}
.follow{position:absolute;right:50px;top:20px;display:flex;align-items:center;gap:14px;font:400 13px "Lato",sans-serif}
.follow i{width:34px;height:34px;border-radius:50%;background:#fff;display:block}
.contact-strip{left:0;top:2154px;width:1200px;height:142px;background:var(--ink)}
.contact-item{position:absolute;top:32px;display:flex;gap:18px;align-items:flex-start}
.contact-item .dot{width:40px;height:40px;border-radius:50%;background:var(--blue);display:flex;align-items:center;justify-content:center;margin-top:2px}
.contact-item b{display:block;font:700 15px "Lato",sans-serif;margin-bottom:6px}
.contact-item span{font:400 14px "Lato",sans-serif}
.copyright{left:0;top:2256px;width:1200px;text-align:center;font:400 12px "Lato",sans-serif;color:#ddd}
</style>
</head>
<body>

<header class="abs hero">
  <div class="abs hero-photo" role="img" aria-label="Portrait of a bride with bold eye makeup and long dark hair"></div>
  <div class="abs brush-photo" role="img" aria-label="Makeup brushes with bursts of coloured powder"></div>
  <div class="abs topband"></div>

  <svg class="abs nav-diamonds" width="1200" height="729" viewBox="0 0 1200 729">
    <polygon points="0,303 141,444 0,585" fill="rgba(151,184,217,.4)"/>
    <polygon points="141,173 282,314 141,455 0,314" fill="rgba(20,20,20,.55)"/>
    <polygon points="426,165 567,306 426,447 285,306" fill="rgba(122,85,48,.8)"/>
    <polygon points="707,150 848,291 707,432 566,291" fill="rgba(151,184,217,.45)"/>
    <polygon points="283,303 424,444 283,585 142,444" fill="rgba(151,184,217,.4)"/>
    <polygon points="566,303 707,444 566,585 425,444" fill="rgba(25,25,25,.6)"/>
    <polygon points="141,441 282,582 141,723 0,582" fill="rgba(122,85,48,.85)"/>
  </svg>

  <div class="nav-label active" style="left:33px;top:262px">
    <svg width="34" height="32" viewBox="0 0 34 32"><path d="M17 2 2 16h5v14h8v-9h4v9h8V16h5z" fill="#fff"/></svg>HOME</div>
  <div class="nav-label" style="left:326px;top:238px">
    <svg width="48" height="60" viewBox="0 0 48 60"><rect x="6" y="6" width="14" height="50" rx="3" fill="#fff"/><rect x="26" y="28" width="16" height="26" rx="3" fill="#fff"/></svg>GALLERY</div>
  <div class="nav-label" style="left:607px;top:250px">
    <svg width="46" height="40" viewBox="0 0 46 40"><path d="M4 10c0-4 4-6 19-6s19 2 19 6v4h-9v-3H13v3H4z" fill="#fff"/><rect x="8" y="18" width="30" height="18" rx="3" fill="#fff"/></svg>CONTACT US</div>
  <div class="nav-label" style="left:183px;top:362px">
    <svg width="40" height="72" viewBox="0 0 40 72"><circle cx="20" cy="10" r="7" fill="#fff"/><path d="M14 20h12l10 48H4z" fill="#fff"/></svg>SERVICES</div>
  <div class="nav-label" style="left:466px;top:372px">
    <svg width="44" height="56" viewBox="0 0 44 56"><rect x="4" y="4" width="36" height="48" fill="none" stroke="#fff" stroke-width="3"/><path d="M12 16h20M12 24h20M12 32h12" stroke="#fff" stroke-width="3"/></svg>BOOK ME</div>
  <div class="nav-label" style="left:41px;top:512px">
    <svg width="60" height="56" viewBox="0 0 60 56"><path d="M8 50C8 20 22 6 40 6c10 0 16 6 16 14M16 50c0-22 10-34 26-34M26 50c0-14 6-22 18-22" fill="none" stroke="#fff" stroke-width="4"/></svg>ABOUT ME</div>

  <div class="abs mail"><span class="ring-icon"><svg width="14" height="10" viewBox="0 0 14 10"><rect width="14" height="10" fill="#fff"/><path d="M0 0l7 6 7-6" fill="none" stroke="#333" stroke-width="1.2"/></svg></span>hello@lumenlace.example</div>
  <div class="abs phone"><span class="ring-icon"><svg width="16" height="16" viewBox="0 0 24 24"><path d="M6 2l4 5-2 3c1 3 3 5 6 6l3-2 5 4-3 4C10 22 2 14 2 5z" fill="#fff"/></svg></span>123 456 7890</div>
  <div class="abs book-btn">Book Me
    <svg width="22" height="22" viewBox="0 0 24 24"><path d="M3 6v15h15v-8" fill="none" stroke="#222" stroke-width="3"/><path d="M10 14l1-4 9-9 3 3-9 9z" fill="#222"/></svg></div>
  <div class="abs brand"><i></i><span>Lumen &amp; Lace</span></div>

  <h1 class="abs headline">We Provide The Services For<br>Hair And Makeup</h1>
  <div class="abs dots"><i></i><i class="on"></i><i></i></div>
</header>

<section class="abs services">
  <div class="service" style="left:51px"><div class="badge"><div>
    <svg width="80" height="80" viewBox="0 0 80 80"><path d="M40 8C28 28 20 40 20 52a20 20 0 0 0 40 0C60 40 52 28 40 8z" fill="#111"/></svg></div></div><h3>Facial</h3></div>
  <div class="service" style="left:277px"><div class="badge"><div>
    <svg width="90" height="90" viewBox="0 0 90 90"><circle cx="22" cy="68" r="10" fill="none" stroke="#111" stroke-width="5"/><circle cx="36" cy="78" r="8" fill="none" stroke="#111" stroke-width="5"/><path d="M28 60 78 10M40 70 80 30" stroke="#111" stroke-width="6"/><rect x="14" y="14" width="46" height="10" transform="rotate(45 37 19)" fill="#111"/></svg></div></div><h3>Hair Cut</h3></div>
  <div class="service" style="left:506px"><div class="badge"><div>
    <svg width="90" height="80" viewBox="0 0 90 80"><ellipse cx="45" cy="26" rx="36" ry="10" fill="#111"/><rect x="9" y="34" width="72" height="34" rx="8" fill="#111"/></svg></div></div><h3>Skincare</h3></div>
  <div class="service" style="left:735px"><div class="badge"><div>
    <svg width="90" height="90" viewBox="0 0 90 90"><circle cx="50" cy="38" r="26" fill="none" stroke="#111" stroke-width="6"/><path d="M30 58 10 80" stroke="#111" stroke-width="8"/></svg></div></div><h3>Makeup</h3></div>
  <div class="service" style="left:963px"><div class="badge"><div>
    <svg width="90" height="80" viewBox="0 0 90 80"><path d="M8 20h44v22H32l-6 28H16l4-28H8z" fill="#111"/><path d="M50 70 84 14" stroke="#111" stroke-width="8"/></svg></div></div><h3>Straighting</h3></div>

  <div class="abs slider-rule" style="top:370px"></div>
  <div class="abs arrow" style="left:562px;top:353px"><svg width="12" height="14" viewBox="0 0 12 14"><path d="M3 2l6 5-6 5" fill="none" stroke="#fff" stroke-width="2"/></svg></div>
  <div class="abs arrow" style="left:618px;top:353px"><svg width="12" height="14" viewBox="0 0 12 14"><path d="M9 2 3 7l6 5" fill="none" stroke="#fff" stroke-width="2"/></svg></div>
</section>

<section class="abs about">
  <div class="abs portrait" role="img" aria-label="Portrait of the bridal stylist"></div>
  <h2 class="abs">ABOUT ME</h2>
  <div class="abs title-rule"></div>
  <div class="abs copy">
    <p>Lorem ipsum dolor sit amet, consectetuer adipiscing elit, sed diam nonummy nibh euismod tincidunt ut laoreet dolore magna aliquam erat volutpat. Ut wisi enim ad minim veniam, quis nostrud exerci tation ullamcorper suscipit lobortis nisl ut aliquip ex ea commodo consequat.</p>
    <p>Lorem ipsum dolor sit amet, consectetuer adipiscing elit, sed diam nonummy nibh euismod tincidunt ut laoreet dolore magna aliquam erat volutpat. Ut wisi enim ad minim veniam, quis nostrud exerci tation ullamcorper suscipit lobortis nisl ut aliquip ex ea commodo consequat. Duis autem vel eum iriure dolor in hendrerit in vulputate velit esse molestie cons</p>
  </div>
</section>

<section class="gallery">
  <h2 class="abs">MY GALLERY</h2>
  <div class="shot" style="left:49px;top:1632px;width:397px;height:337px;background:linear-gradient(135deg,#3a2618,#9a6a3c 60%,#c08a4c)" role="img" aria-label="Bride applying lipstick in front of a mirror"></div>
  <div class="shot" style="left:455px;top:1632px;width:413px;height:158px;background:linear-gradient(90deg,#1f3b46,#d6b6a2 50%,#1c3a44)" role="img" aria-label="Close-up of closed eyes with smoky eye makeup"></div>
  <div class="shot" style="left:455px;top:1799px;width:203px;height:170px;background:linear-gradient(135deg,#e8d6cc,#c98f86)" role="img" aria-label="Eyeliner being applied with a brush"></div>
  <div class="shot" style="left:668px;top:1799px;width:200px;height:170px;background:linear-gradient(135deg,#5fb6cf,#d8a894 60%,#f0e6e2)" role="img" aria-label="Model with vivid blue eye makeup"></div>
  <div class="shot" style="left:877px;top:1632px;width:268px;height:337px;background:linear-gradient(160deg,#f4f0ec,#e4c4a8 55%,#b8c69a)" role="img" aria-label="Blush brush applied to a woman's cheek"></div>
  <div class="abs slider-rule" style="top:2019px"></div>
  <div class="abs arrow" style="left:562px;top:2002px"><svg width="12" height="14" viewBox="0 0 12 14"><path d="M3 2l6 5-6 5" fill="none" stroke="#fff" stroke-width="2"/></svg></div>
  <div class="abs arrow" style="left:618px;top:2002px"><svg width="12" height="14" viewBox="0 0 12 14"><path d="M9 2 3 7l6 5" fill="none" stroke="#fff" stroke-width="2"/></svg></div>
</section>

<footer>
  <nav class="abs footer-nav">
    <ul><li>HOME</li><li>ABOUT ME</li><li>SERVICES</li><li>GALLERY</li></ul>
    <div class="follow">Follow Us On: <i></i><i></i><i></i></div>
  </nav>
  <div class="abs contact-strip">
    <div class="contact-item" style="left:170px">
      <span class="dot"><svg width="16" height="20" viewBox="0 0 16 20"><path d="M8 0a7 7 0 0 0-7 7c0 5 7 13 7 13s7-8 7-13a7 7 0 0 0-7-7z" fill="#fff"/><circle cx="8" cy="7" r="2.5" fill="#97b8d9"/></svg></span>
      <div><b>Lumen and Lace</b><span>123, Lorewam Dollar, Smit Amet - 123456</span></div>
    </div>
    <div class="contact-item" style="left:585px">
      <span class="dot"><svg width="18" height="18" viewBox="0 0 24 24"><path d="M6 2l4 5-2 3c1 3 3 5 6 6l3-2 5 4-3 4C10 22 2 14 2 5z" fill="#fff"/></svg></span>
      <div><b>Call Us :</b><span>+123 456 7890</span></div>
    </div>
    <div class="contact-item" style="left:831px">
      <span class="dot"><svg width="18" height="13" viewBox="0 0 14 10"><rect width="14" height="10" fill="#fff"/><path d="M0 0l7 6 7-6" fill="none" stroke="#97b8d9" stroke-width="1.2"/></svg></span>
      <div><b>Email Us :</b><span>hello@lumenlace.example</span></div>
    </div>
  </div>
  <p class="abs copyright">© 2016 Lumenandlace.&nbsp; All Rights Reserved.</p>
</footer>

</body>
</html>
```